Fasteners Poly-bag design with KEVRA brand

We are trading with fasteners and rigging hardware and now we need a new design for a poly-bag. The header of poly-bag will contain two parts - top part (around 60%) will be static with our logo "KEVRA" and your type of design. The bottom part (around 40%) should be with different color for each group of fasteners or rigging hardware and with different text (5 groups in total). The border between the two part can be different from straight line (for example like wave or something else). I added a file with explanation and some samples of poly-bags. The total dimensions of the header are 80 mm/40 mm. The nylon part of poly-bag will have a background - I added a file with our image, but you can offer us different image also. Please when creating design, do it for full poly-bag, including the nylon part, not only header. The colors from header can continue to the nylon part also. I added a file "DESIGN SAMPLES" just as examples, what we expect to see. Of course you can offer your own variant of design! Thank you in advance!

Target Market(s)

Fasteners and rigging hardware

Industry/Entity Type

Fastener

Font styles to use
Other font styles liked:
• SAUCER BB - Logo Font

Colors

Designer to choose colors to be used in the design.

Requirements
Must have
• Our logo "KEVRA"

```html
<!DOCTYPE html>
<html lang="en">
<head>
<meta charset="utf-8">
<title>KEVRA Fastener Poly-bags</title>
<link rel="stylesheet" href="https://fonts.googleapis.com/css2?family=Archivo:wght@600;800&display=swap">
<style>
  :root {
    --page-bg: #ececec;
    --brand-red: #e11a24;
    --brand-black: #231f20;
    --steel-light: #d9d9d9;
    --steel-mid: #b9b9b9;
    --steel-dark: #9e9e9e;
    --nylon-light: #f7f7f7;
    --nylon-mid: #e4e4e4;
    --group-green: #39b54a;
    --group-orange: #f26522;
    --label-ink: #2a2a2a;
  }
  * { margin: 0; padding: 0; box-sizing: border-box; }
  html, body { width: 1200px; height: 978px; overflow: hidden; background: var(--page-bg); }
  .canvas { position: relative; width: 1200px; height: 978px; }

  .polybag {
    position: absolute;
    top: 166px;
    width: 390px;
    height: 646px;
    overflow: hidden;
    background: var(--nylon-light);
  }
  .polybag--hex { left: 181px; }
  .polybag--torx { left: 646px; }

  .nylon {
    position: absolute; inset: 0;
    background:
      radial-gradient(ellipse at 60% 35%, #ffffff 0%, transparent 55%),
      linear-gradient(160deg, var(--nylon-light) 0%, var(--nylon-mid) 60%, #eeeeee 100%);
  }
  .stripe { position: absolute; top: 0; bottom: 0; }
  .stripe--red { left: 0; width: 63px; background: var(--brand-red); }
  .stripe--black { left: 63px; width: 22px; background: var(--brand-black); }

  .header-steel {
    position: absolute; left: 85px; right: 0; top: 0; height: 148px;
    background:
      repeating-linear-gradient(0deg, rgba(255,255,255,0.08) 0 1px, rgba(0,0,0,0.04) 1px 2px),
      linear-gradient(100deg, var(--steel-dark) 0%, var(--steel-light) 35%, var(--steel-mid) 60%, var(--steel-light) 85%, var(--steel-dark) 100%);
  }
  .hang-hole { position: absolute; left: 50px; top: 22px; }

  .brand-name {
    position: absolute; left: 52px; top: 82px;
    font-family: "Archivo", sans-serif;
    font-weight: 800;
    font-size: 56px;
    letter-spacing: 2px;
    line-height: 1;
    color: var(--brand-black);
  }

  .group-band {
    position: absolute; left: 0; right: 0; top: 148px; height: 47px;
    display: flex; align-items: center; justify-content: center;
    font-family: "Archivo", sans-serif;
    font-weight: 600;
    font-size: 14.5px;
    color: var(--label-ink);
    letter-spacing: -0.2px;
  }
  .group-band--green { background: var(--group-green); }
  .group-band--orange { background: var(--group-orange); }
</style>
</head>
<body>
<main class="canvas">

  <section class="polybag polybag--hex">
    <div class="nylon" role="img" aria-label="Clear nylon bag window with soft plastic sheen"></div>
    <div class="stripe stripe--red"></div>
    <div class="stripe stripe--black"></div>
    <div class="header-steel">
      <svg class="hang-hole" width="122" height="40" viewBox="0 0 122 40" aria-hidden="true">
        <path d="M10 22 H44 A17 17 0 0 1 78 22 H112 A8 8 0 0 1 112 38 H10 A8 8 0 0 1 10 22 Z" fill="var(--page-bg)"/>
      </svg>
      <div class="brand-name">KEVRA</div>
    </div>
    <div class="group-band group-band--green">HEX BOLT FULL THREAD M6 X 6MM - STAINLESS</div>
  </section>

  <section class="polybag polybag--torx">
    <div class="nylon" role="img" aria-label="Clear nylon bag window with soft plastic sheen"></div>
    <div class="stripe stripe--red"></div>
    <div class="stripe stripe--black"></div>
    <div class="header-steel">
      <svg class="hang-hole" width="122" height="40" viewBox="0 0 122 40" aria-hidden="true">
        <path d="M10 22 H44 A17 17 0 0 1 78 22 H112 A8 8 0 0 1 112 38 H10 A8 8 0 0 1 10 22 Z" fill="var(--page-bg)"/>
      </svg>
      <div class="brand-name">KEVRA</div>
    </div>
    <div class="group-band group-band--orange">TORX CAP SCREW M5 X 6MM - STAINLESS</div>
  </section>

</main>
</body>
</html>
```